Financial Advisory Firm needs a custom content template for financial topics

I need a template that I can reuse often to deliver financial advice commentary on topics ranging from investments to financial planning ideas to tax planning strategies. I am hoping to get a template that is visually exciting and captures readers attention. I will use this template to regularly create new financial and tax content that I will post to social media (e.g. Quorvex), my website and targeted email campaigns to current and prospective clients. The content will never be greater than 2 pages.

```html
<!DOCTYPE html>
<html lang="en">
<head>
<meta charset="utf-8">
<title>2021 Income Tax Planning Flyer</title>
<link rel="stylesheet" href="https://fonts.googleapis.com/css2?family=Oswald:wght@600&family=Roboto:wght@400;700&display=swap">
<style>
  :root {
    --page-bg: #e9ebed;
    --paper: #ffffff;
    --brand-blue: #1467ad;
    --brand-blue-dark: #0f5a97;
    --heading-blue: #1a6db4;
    --accent-yellow: #e9c55a;
    --ink: #1e1e1e;
  }
  * { box-sizing: border-box; margin: 0; padding: 0; }
  html, body { width: 1200px; height: 1200px; overflow: hidden; }
  body { background: var(--page-bg); font-family: "Roboto", Arial, sans-serif; color: var(--ink); }

  .flyer { position: absolute; left: 150px; top: 21px; width: 900px; height: 1158px; background: var(--paper); overflow: hidden; }

  .hero-photo { position: absolute; left: 0; top: 0; width: 900px; height: 392px;
    background: linear-gradient(100deg, #3b3f45 0%, #6d6a66 28%, #c9b9a6 52%, #f1e6d8 72%, #f7efe6 100%); }

  .brand { position: absolute; right: 58px; top: 74px; display: flex; align-items: center; gap: 10px;
    font-family: "Roboto", Arial, sans-serif; font-weight: 700; font-size: 30px; color: var(--brand-blue); }
  .brand-dot { width: 22px; height: 22px; border-radius: 50%; background: var(--brand-blue); }

  .title-accent { position: absolute; left: 10px; top: 251px; width: 376px; height: 401px; background: var(--accent-yellow); }
  .title-block { position: absolute; left: 25px; top: 216px; width: 375px; height: 402px; background: var(--brand-blue);
    padding: 50px 0 0 20px; color: #fff; font-family: "Oswald", Impact, sans-serif; font-weight: 600; overflow: hidden; }
  .title-year { font-size: 70px; line-height: 74px; }
  .title-main { font-size: 47px; line-height: 60px; margin-top: 2px; letter-spacing: -0.4px; white-space: nowrap; }

  .section-heading { color: var(--heading-blue); font-weight: 700; font-size: 20px; letter-spacing: 0.2px; }
  .sub-heading { color: var(--heading-blue); font-weight: 700; font-size: 16px; margin: 14px 0 10px; }

  .known { position: absolute; left: 427px; top: 412px; width: 450px; }
  .known-list { list-style: none; margin-top: 14px; }
  .known-list li { position: relative; padding-left: 50px; font-size: 14px; line-height: 16px; margin-bottom: 10px; }
  .num { position: absolute; left: 14px; top: 0; width: 18px; height: 18px; border: 2px solid var(--brand-blue); border-radius: 50%;
    font-size: 11px; font-weight: 700; line-height: 14px; text-align: center; color: #111; }

  .thoughts { position: absolute; left: 23px; top: 680px; width: 375px; }
  .thought-list { list-style: none; margin-top: 14px; }
  .thought-list li { position: relative; padding-left: 20px; font-size: 13px; line-height: 15.4px; margin-bottom: 15px; }
  .thought-list svg { position: absolute; left: 0; top: 2px; }

  .quote { position: absolute; left: 45px; top: 1000px; width: 340px; font-size: 13px; line-height: 15.4px; }
  .quote-rule { display: flex; align-items: center; justify-content: center; gap: 8px; margin: 0 30px 14px 20px; }
  .quote-rule span { flex: 1; height: 2px; background: var(--brand-blue); }
  .quote-mark { color: var(--brand-blue); font-weight: 700; font-size: 34px; line-height: 20px; height: 14px; }
  .quote-source { color: var(--heading-blue); }

  .proposals { position: absolute; left: 435px; top: 680px; width: 445px; }
  .proposals .section-heading { margin-bottom: -4px; }
  .check-list { list-style: none; }
  .check-list li { position: relative; padding-left: 41px; font-size: 13px; line-height: 15.4px; margin-bottom: 12px; }
  .check-list svg { position: absolute; left: 4px; top: 2px; }

  .footer-rule { position: absolute; left: 0; top: 1080px; width: 900px; height: 7px; background: var(--accent-yellow); }
  .footer { position: absolute; left: 0; top: 1087px; width: 900px; height: 71px; background: var(--brand-blue-dark);
    color: #fff; font-size: 14px; }
  .contact { position: absolute; top: 0; height: 71px; display: flex; align-items: center; gap: 12px; line-height: 17px; white-space: nowrap; }
  .contact.address { left: 46px; gap: 14px; }
  .contact.phone { left: 316px; }
  .contact.email { left: 506px; }
  .contact.web { left: 704px; }
</style>
</head>
<body>
<main class="flyer">
  <div class="hero-photo" role="img" aria-label="Photo of two people reviewing printed financial charts beside a laptop and coffee cup on a sunlit desk"></div>

  <div class="brand"><span class="brand-dot"></span>Northmark Finance</div>

  <div class="title-accent"></div>
  <h1 class="title-block">
    <div class="title-year">2021</div>
    <div class="title-main">INCOME TAX<br>PLANNING<br>FOR THE HARLAN<br>ADMINISTRATION</div>
  </h1>

  <section class="known">
    <h2 class="section-heading">WHAT DO WE KNOW?</h2>
    <ol class="known-list">
      <li><span class="num">1</span>The Harlan administration has proposed multiple trillions of dollars in additional spending.</li>
      <li><span class="num">2</span>Proposed ordinary income tax rate increase for taxpayers with income &gt; $400,000</li>
      <li><span class="num">3</span>Proposed changes to long-term capital gain tax rates for taxpayers with income &gt; $1,000,000.</li>
      <li><span class="num">4</span>Proposed rates higher than income taxes</li>
      <li><span class="num">5</span>Proposed limit to itemized deductions to 28% of income</li>
      <li><span class="num">6</span>Proposed replacement of Retirement account contribution deduction with a 26% credit.</li>
    </ol>
  </section>

  <section class="thoughts">
    <h2 class="section-heading">KEY PLANNING THOUGHTS</h2>
    <ul class="thought-list">
      <li><svg width="13" height="13" viewBox="0 0 13 13"><circle cx="6.5" cy="6.5" r="5.7" fill="none" stroke="#1467ad" stroke-width="1"/><path d="M3.8 6.6l1.8 1.8 3.5-3.6" fill="none" stroke="#1467ad" stroke-width="1.1"/></svg>If there was ever a time to get your financial house in order, now is the time. With multiple proposals for tax increases to potentially at the end of the year. Now is an important time to take action.</li>
      <li><svg width="13" height="13" viewBox="0 0 13 13"><circle cx="6.5" cy="6.5" r="5.7" fill="none" stroke="#1467ad" stroke-width="1"/><path d="M3.8 6.6l1.8 1.8 3.5-3.6" fill="none" stroke="#1467ad" stroke-width="1.1"/></svg>Roth conversions are a strategy to accelerate income, however there are now no options to undo conversions due to the elimination of Roth recharacterizations.</li>
      <li><svg width="13" height="13" viewBox="0 0 13 13"><circle cx="6.5" cy="6.5" r="5.7" fill="none" stroke="#1467ad" stroke-width="1"/><path d="M3.8 6.6l1.8 1.8 3.5-3.6" fill="none" stroke="#1467ad" stroke-width="1.1"/></svg>Opportunities to harvest ordinary income and capital gains should be considered based on your individual situation to act as 'insurance' against tax increases.</li>
      <li><svg width="13" height="13" viewBox="0 0 13 13"><circle cx="6.5" cy="6.5" r="5.7" fill="none" stroke="#1467ad" stroke-width="1"/><path d="M3.8 6.6l1.8 1.8 3.5-3.6" fill="none" stroke="#1467ad" stroke-width="1.1"/></svg>High-income taxpayers with income above the 28% tax bracket who already itemize may benefit from accelerated additional itemized deductions before year-end 2021 as the proposed 28% cap would limit future itemized deductions.</li>
    </ul>
  </section>

  <blockquote class="quote">
    <div class="quote-rule"><span></span><b class="quote-mark">&ldquo;</b><span></span></div>
    According to tax returns filed through the first 30 weeks of year, 9.6% of filers chose to itemize their deductions on their 2019 tax returns. <span class="quote-source">- Fiscal Data Institute</span>
  </blockquote>

  <section class="proposals">
    <h2 class="section-heading">KEY PROPOSALS IN HARLAN'S PLATFORM</h2>
    <h3 class="sub-heading">Ordinary Income</h3>
    <ul class="check-list">
      <li><svg width="18" height="15" viewBox="0 0 18 15"><rect x="1" y="3" width="12" height="11" fill="none" stroke="#1467ad" stroke-width="1.6"/><path d="M4 8l3 3 9-10" fill="none" stroke="#1467ad" stroke-width="2"/></svg>Proposed top tax bracket of 39.6%, same as before the Tax Cuts &amp; Jobs Act (TCJA)</li>
      <li><svg width="18" height="15" viewBox="0 0 18 15"><rect x="1" y="3" width="12" height="11" fill="none" stroke="#1467ad" stroke-width="1.6"/><path d="M4 8l3 3 9-10" fill="none" stroke="#1467ad" stroke-width="2"/></svg>Proposed ordinary income tax rate increase for taxpayers with income &gt; $400,000</li>
      <li><svg width="18" height="15" viewBox="0 0 18 15"><rect x="1" y="3" width="12" height="11" fill="none" stroke="#1467ad" stroke-width="1.6"/><path d="M4 8l3 3 9-10" fill="none" stroke="#1467ad" stroke-width="2"/></svg>Elimination of the Qualified Business Income (QBI) deduction for those making over $400,000/yr</li>
    </ul>
    <h3 class="sub-heading">Itemized Deductions</h3>
    <ul class="check-list">
      <li><svg width="18" height="15" viewBox="0 0 18 15"><rect x="1" y="3" width="12" height="11" fill="none" stroke="#1467ad" stroke-width="1.6"/><path d="M4 8l3 3 9-10" fill="none" stroke="#1467ad" stroke-width="2"/></svg>Proposed cap on the limit for deductions. This would limit the maximum benefit to the 28% tax bracket.</li>
      <li><svg width="18" height="15" viewBox="0 0 18 15"><rect x="1" y="3" width="12" height="11" fill="none" stroke="#1467ad" stroke-width="1.6"/><path d="M4 8l3 3 9-10" fill="none" stroke="#1467ad" stroke-width="2"/></svg>The cap would limit the value of itemized deductions. (i.e. if taxpayers were in the 32%, 35% or 39.6% bracket, they would only receive a 28% break on their itemized.</li>
    </ul>
    <h3 class="sub-heading">Planning</h3>
    <ul class="check-list">
      <li><svg width="18" height="15" viewBox="0 0 18 15"><rect x="1" y="3" width="12" height="11" fill="none" stroke="#1467ad" stroke-width="1.6"/><path d="M4 8l3 3 9-10" fill="none" stroke="#1467ad" stroke-width="2"/></svg>Higher taxes for the "wealthy" are just around the corner. Work with you CPA and financial planner to set yourself up for financial success.</li>
    </ul>
  </section>

  <div class="footer-rule"></div>
  <footer class="footer">
    <div class="contact address">
      <svg width="22" height="24" viewBox="0 0 22 24"><path d="M11 1a9 9 0 0 0-9 9c0 6 9 13 9 13s9-7 9-13a9 9 0 0 0-9-9z" fill="#e9c55a"/><circle cx="11" cy="10" r="3.5" fill="#0f5a97"/></svg>
      <span>418 Alder Avenue, Suite 210<br>Brookhaven, WA 98000</span>
    </div>
    <div class="contact phone">
      <svg width="20" height="20" viewBox="0 0 20 20"><circle cx="10" cy="10" r="9" fill="none" stroke="#e9c55a" stroke-width="1.4"/><path d="M7 5.5l1.5 2.5-1 1.2c.7 1.5 1.8 2.6 3.3 3.3l1.2-1 2.5 1.5-.8 1.6c-3.8-.3-7-3.5-7.3-7.3z" fill="#e9c55a"/></svg>
      <span>(555) 014-2290</span>
    </div>
    <div class="contact email">
      <svg width="20" height="14" viewBox="0 0 20 14"><rect x="0.5" y="0.5" width="19" height="13" fill="#e9c55a"/><path d="M1 1l9 7 9-7M1 13l6.5-6M19 13l-6.5-6" fill="none" stroke="#0f5a97" stroke-width="1.2"/></svg>
      <span>hello@northmarkfin.com</span>
    </div>
    <div class="contact web">
      <svg width="16" height="16" viewBox="0 0 16 16" fill="none" stroke="#e9c55a" stroke-width="1.1"><circle cx="8" cy="8" r="7"/><ellipse cx="8" cy="8" rx="3" ry="7"/><path d="M1 8h14M2.5 4h11M2.5 12h11"/></svg>
      <span>www.northmarkfin.com</span>
    </div>
  </footer>
</main>
</body>
</html>
```